Business Card Design for Cybersecurity Company - Quorvent Systems

We need a business card design for our new cybersecurity company, Quorvent. We’re going for a clean, hi tech look that feels modern, premium, and trustworthy. We want a design that really stands out and makes people say WOW when we hand it over!

Quorvent delivers reliable IT support and managed services for small and mid sized businesses. We help companies stay secure, efficient, and connected through proactive monitoring, cybersecurity services, cloud management, and remote support.

Target Market(s)

Designers should target small and mid sized businesses that need dependable cybersecurity and IT support.

Industry/Entity Type

Cybersecurity, Managed Service Provider, IT services

Contact Information for Business Card

Contact information

Requirements
Must have
• The card should look clean, modern, and tech focused, with the Quorvent logo, clear contact info, and strong readability. It needs to feel premium and professional while still keeping a simple layout that fits a cybersecurity and IT brand.
Nice to have
• Nice to have elements include subtle touches that give the card a modern, tech feel, along with a layout that works well in different background styles.
Should not have
• The card should avoid clutter, loud graphics, or anything that takes attention away from the logo and contact details.

```html
<!DOCTYPE html>
<html lang="en">
<head>
<meta charset="utf-8">
<title>Quorvent Systems – Business Card</title>
<link href="https://fonts.googleapis.com/css2?family=Arimo:wght@400;700&display=swap" rel="stylesheet">
<style>
  :root {
    --page-bg: #e4e4e6;
    --card-blue: #2f6bff;
    --card-violet: #7a1bd4;
    --card-white: #ffffff;
    --ink-light: #ffffff;
    --brand-ink: #4b4ce6;
    --mark-tint: rgba(255, 255, 255, 0.14);
  }
  * { box-sizing: border-box; margin: 0; padding: 0; }
  html, body {
    width: 1200px;
    height: 1200px;
    overflow: hidden;
    background: var(--page-bg);
    font-family: "Arimo", Arial, sans-serif;
  }
  .card {
    position: absolute;
    width: 688px;
    height: 393px;
  }
  .card-front {
    left: 266px;
    top: 158px;
    background: radial-gradient(ellipse 55% 75% at 50% 52%, var(--card-violet) 0%, #5a3be6 45%, var(--card-blue) 100%);
    color: var(--ink-light);
  }
  .card-back {
    left: 262px;
    top: 653px;
    background: var(--card-white);
    display: flex;
    align-items: center;
    justify-content: center;
    gap: 20px;
  }
  .brand-name {
    font-weight: 700;
    white-space: nowrap;
  }
  .card-front .brand-name {
    position: absolute;
    left: 44px;
    top: 60px;
    font-size: 34px;
    line-height: 1;
    color: var(--ink-light);
  }
  .brand-mark {
    position: absolute;
    left: 346px;
    top: 40px;
    width: 300px;
    height: 300px;
    border-radius: 50%;
    background: var(--mark-tint);
    display: flex;
    align-items: center;
    justify-content: center;
  }
  .brand-mark .brand-name {
    font-size: 46px;
    color: var(--ink-light);
  }
  .card-back .brand-dot {
    width: 110px;
    height: 110px;
    border-radius: 50%;
    background: var(--brand-ink);
    flex-shrink: 0;
  }
  .card-back .brand-name {
    font-size: 44px;
    color: var(--brand-ink);
  }
  .person {
    position: absolute;
    left: 44px;
    top: 170px;
  }
  .person-name {
    font-size: 25px;
    font-weight: 700;
    line-height: 1.1;
  }
  .person-role {
    font-size: 15px;
    margin-top: 3px;
  }
  .contact-list {
    position: absolute;
    left: 44px;
    top: 418px;
    top: 260px;
    list-style: none;
  }
  .contact-item {
    display: flex;
    align-items: center;
    height: 20.5px;
    font-size: 16px;
  }
  .contact-icon {
    width: 14px;
    height: 14px;
    margin-right: 13px;
    flex-shrink: 0;
  }
</style>
</head>
<body>
  <section class="card card-front" aria-label="Business card front">
    <div class="brand-name">Quorvent Systems</div>

    <div class="person">
      <div class="person-name">Dana Whitfield</div>
      <div class="person-role">Owner | CEO</div>
    </div>

    <ul class="contact-list">
      <li class="contact-item">
        <svg class="contact-icon" viewBox="0 0 24 24" aria-hidden="true"><path fill="#fff" d="M6.6 10.8a15.1 15.1 0 0 0 6.6 6.6l2.2-2.2a1 1 0 0 1 1-.25 11.4 11.4 0 0 0 3.6.57 1 1 0 0 1 1 1V20a1 1 0 0 1-1 1A17 17 0 0 1 3 4a1 1 0 0 1 1-1h3.5a1 1 0 0 1 1 1c0 1.25.2 2.45.57 3.57a1 1 0 0 1-.25 1z"/></svg>
        (855) 555-QVNT
      </li>
      <li class="contact-item">
        <svg class="contact-icon" viewBox="0 0 24 24" aria-hidden="true"><rect x="6" y="1.5" width="12" height="21" rx="2" fill="none" stroke="#fff" stroke-width="2.4"/><rect x="10" y="18" width="4" height="1.6" fill="#fff"/></svg>
        (813) 555-0142
      </li>
      <li class="contact-item">
        <svg class="contact-icon" viewBox="0 0 24 24" aria-hidden="true"><rect x="2" y="5" width="20" height="14" fill="#fff"/><path d="M2 5l10 8 10-8" fill="none" stroke="#5a3be6" stroke-width="1.8"/></svg>
        dana@quorvent.com
      </li>
      <li class="contact-item">
        <svg class="contact-icon" viewBox="0 0 24 24" aria-hidden="true"><circle cx="12" cy="12" r="10" fill="#fff"/><path d="M8 6c2 1 1 3 3 4s0 3 2 4 1 4 0 6M15 4c0 2 2 3 4 3" fill="none" stroke="#4d56ee" stroke-width="1.8"/></svg>
        www.quorvent.com
      </li>
    </ul>

    <div class="brand-mark" role="img" aria-label="Quorvent brand mark area">
      <span class="brand-name">Quorvent</span>
    </div>
  </section>

  <section class="card card-back" aria-label="Business card back">
    <span class="brand-dot" aria-hidden="true"></span>
    <div class="brand-name">Quorvent Systems</div>
  </section>
</body>
</html>
```